Email Banner for Technology Company

We need a new email banner. The purpose of the email banner is to make us look more professional as a business and keep all communications with clients uniform. The previous designs which we have included below have now become outdated as our brand has developed and we need the new banner to become more aligned and modern.
We are a marketing organization that specialises in lead generation, email newsletters are sent to prospects on a regular basis. Therefore, it is important that we have an aesthetically pleasing banner as this is the first real impression prospects have our business. First impressions matter.
We are looking for a new email banner design as the current design is now outdated and does not reflect who we are as a business.
The new banners are required for launch at the start of Q2.
There is future work in the pipeline for the winning design. We have multiple industry sites that will require the new design as well as creating each of these in multiple languages.
The design must include the Lumenfield Dossiers wording the tagline 'The Technology Pro’s Research Hub'.
It needs to be creative and fun but still remain professional, sticking with the colour theme that already exists.

```html
<!DOCTYPE html>
<html lang="en">
<head>
<meta charset="utf-8">
<title>Lumenfield Dossiers – Email Banners</title>
<link href="https://fonts.googleapis.com/css2?family=Montserrat:wght@300;700&display=swap" rel="stylesheet">
<style>
  :root {
    --navy: #021f3d;
    --teal: #063f5a;
    --deep: #04294a;
    --blue: #0093d6;
    --white: #ffffff;
    --ink: #0c2a47;
    --logo-ink: #111111;
  }
  html, body {
    margin: 0;
    padding: 0;
    width: 1200px;
    height: 779px;
    overflow: hidden;
    background: var(--white);
  }
  .sheet {
    position: relative;
    width: 1200px;
    height: 779px;
  }
  .banner {
    position: absolute;
    left: 65.5px;
    width: 1069px;
    height: 178.5px;
    overflow: hidden;
    font-family: 'Montserrat', sans-serif;
  }
  .banner--dark { top: 61px; }
  .banner--azure { top: 300.5px; }
  .banner--split { top: 540px; }
  .banner__art {
    position: absolute;
    inset: 0;
    width: 100%;
    height: 100%;
    display: block;
  }
  .wordmark {
    position: absolute;
    transform: translate(-50%, -50%);
    margin: 0;
    font-weight: 700;
    white-space: nowrap;
    letter-spacing: -0.3px;
  }
  .banner--dark .wordmark { left: 190px; top: 90px; font-size: 21px; color: var(--logo-ink); }
  .banner--azure .wordmark { left: 190px; top: 90px; font-size: 21px; color: var(--white); }
  .banner--split .wordmark { left: 248px; top: 113px; font-size: 27px; color: var(--white); }
  .tagline {
    position: absolute;
    margin: 0;
    color: var(--white);
    font-weight: 300;
    white-space: nowrap;
    letter-spacing: 0.2px;
  }
  .tagline strong { font-weight: 700; }
  .tagline--inline {
    left: 711px;
    top: 99px;
    transform: translate(-50%, -50%);
    font-size: 26.5px;
  }
  .tagline--stacked {
    left: 625px;
    top: 70px;
    font-size: 25.5px;
    line-height: 29px;
  }
  .tagline--stacked strong { display: block; }
  .cta {
    position: absolute;
    left: 1004px;
    top: 14px;
    transform: translate(-50%, -50%);
    font-size: 15px;
    font-weight: 700;
    color: var(--ink);
    letter-spacing: 0.4px;
    text-decoration: none;
    white-space: nowrap;
  }
</style>
</head>
<body>
<main class="sheet">

  <!-- Banner 1: navy panel, dark field -->
  <section class="banner banner--dark">
    <svg class="banner__art" viewBox="0 0 2120 354" preserveAspectRatio="none">
      <defs>
        <linearGradient id="fieldDark" x1="0" y1="0" x2="0" y2="1">
          <stop offset="0" stop-color="#053a55"/>
          <stop offset="1" stop-color="#04294a"/>
        </linearGradient>
      </defs>
      <g role="img" aria-label="Subtle grid texture">
        <rect width="2120" height="354" fill="url(#fieldDark)"/>
      </g>
      <rect width="772" height="354" fill="#021f3d"/>
      <rect x="0" y="120" width="760" height="112" fill="#ffffff"/>
      <path d="M1870,0 H2120 V57 H1882 L1870,48 Z" fill="#ffffff"/>
    </svg>
    <p class="wordmark">Lumenfield Dossiers</p>
    <p class="tagline tagline--inline">The Technology Pro’s <strong>Research Hub</strong></p>
    <a class="cta" href="#">CLICK HERE</a>
  </section>

  <!-- Banner 2: navy panel, azure field -->
  <section class="banner banner--azure">
    <svg class="banner__art" viewBox="0 0 2120 354" preserveAspectRatio="none">
      <defs>
        <linearGradient id="fieldAzure" x1="0" y1="0" x2="0" y2="1">
          <stop offset="0" stop-color="#04365a"/>
          <stop offset="0.45" stop-color="#03659a"/>
          <stop offset="1" stop-color="#0093d6"/>
        </linearGradient>
      </defs>
      <g role="img" aria-label="Subtle grid texture">
        <rect width="2120" height="354" fill="url(#fieldAzure)"/>
      </g>
      <rect width="772" height="354" fill="#021f3d"/>
      <rect x="0" y="120" width="760" height="112" fill="#0093d6"/>
      <path d="M1870,0 H2120 V57 H1882 L1870,48 Z" fill="#ffffff"/>
    </svg>
    <p class="wordmark">Lumenfield Dossiers</p>
    <p class="tagline tagline--inline">The Technology Pro’s <strong>Research Hub</strong></p>
    <a class="cta" href="#">CLICK HERE</a>
  </section>

  <!-- Banner 3: split field with a soft diagonal band -->
  <section class="banner banner--split">
    <svg class="banner__art" viewBox="0 0 2120 354" preserveAspectRatio="none">
      <defs>
        <linearGradient id="fieldRight" x1="0" y1="0" x2="0" y2="1">
          <stop offset="0" stop-color="#073a57"/>
          <stop offset="1" stop-color="#04294a"/>
        </linearGradient>
        <linearGradient id="bandSoft" x1="0" y1="0" x2="1" y2="0">
          <stop offset="0" stop-color="#0093d6"/>
          <stop offset="1" stop-color="#021f3d"/>
        </linearGradient>
      </defs>
      <rect width="2120" height="354" fill="#063f5a"/>
      <g role="img" aria-label="Soft texture on the right field">
        <polygon points="905,0 2120,0 2120,354 1110,354" fill="url(#fieldRight)"/>
      </g>
      <g role="img" aria-label="Diagonal accent band">
        <polygon points="800,0 905,0 1110,354 1005,354" fill="url(#bandSoft)" opacity="0.85"/>
      </g>
      <path d="M1864,0 H2120 V57 H1890 Q1864,57 1864,31 Z" fill="#ffffff"/>
    </svg>
    <p class="wordmark">Lumenfield Dossiers</p>
    <p class="tagline tagline--stacked">The Technology Pro’s <strong>Research Hub</strong></p>
    <a class="cta" href="#">CLICK HERE</a>
  </section>

</main>
</body>
</html>
```